A small boutique Accounting and Mortgage Broking firm needs a business card design

Quorvel is a Brisbane based boutique accounting and mortgage broking firm. We offer a range of extensive financial services like accounting, tax consulting, book-keeping and mortgage broking.
We need a business card that stands out. The content can stay as it is on the existing card unless you recommend us to change anything on it for a better design.
Please remove the mobile number and give us a suitable format to change the details like email address and name.
Industry/Entity Type
Business
Contact Information for Business Card
Dalian Okoruwe
Quorvel Group Pty Ltd
3/412 Brackwin Rd Halvern QLD 4219
PO Box 829 Halvern QLD 4219
T 07 3184 5526
F 07 3952 1087
E dokoruwe@quorvel.net.au
Accountants Tax Agents, Mortgage Brokers
www.quorvel.net.au
Look and feel
Each slider illustrates characteristics of the customer's brand and the style your logo design should communicate.

```html
<!DOCTYPE html>
<html lang="en">
<head>
<meta charset="utf-8">
<title>Quorvel Business Card</title>
<link href="https://fonts.googleapis.com/css2?family=Arimo:wght@400;700&display=swap" rel="stylesheet">
<style>
  :root {
    --brand-green: #7dc242;
    --ink: #333436;
    --paper: #ffffff;
    --backdrop: #2a2a2b;
  }
  * { margin: 0; padding: 0; box-sizing: border-box; }
  html, body {
    width: 1200px; height: 1189px; overflow: hidden;
    background: var(--backdrop);
    font-family: "Arimo", Arial, sans-serif;
  }
  .card {
    position: absolute; left: 160px;
    width: 880px; height: 503px;
    border-radius: 26px;
    overflow: hidden;
  }
  /* Front */
  .card-front { top: 60px; background: var(--brand-green); }
  .front-brand {
    position: absolute; left: 0; right: 0; top: 120px;
    display: flex; align-items: center; justify-content: center; gap: 28px;
  }
  .brand-dot {
    border-radius: 50%;
    border: solid var(--ink);
    flex: none;
  }
  .front-brand .brand-dot { width: 130px; height: 130px; border-width: 16px; }
  .front-brand .brand-name {
    font-size: 112px; font-weight: 700; color: var(--ink); letter-spacing: -2px; line-height: 1;
  }
  .front-tagline {
    position: absolute; left: 0; right: 0; top: 290px; text-align: center;
    font-size: 42px; font-weight: 400; color: var(--ink); letter-spacing: 3px;
  }
  .front-services {
    position: absolute; left: 0; right: 0; top: 370px; text-align: center;
    font-size: 24px; font-weight: 700; color: var(--paper); letter-spacing: 0.5px;
  }
  /* Back */
  .card-back { top: 626px; background: var(--paper); }
  .back-brand {
    position: absolute; left: 44px; top: 48px;
    display: flex; align-items: center; gap: 18px;
  }
  .back-brand .brand-dot { width: 92px; height: 92px; border-width: 11px; }
  .back-brand .brand-name {
    font-size: 76px; font-weight: 700; color: var(--brand-green); letter-spacing: -1px; line-height: 1;
  }
  .back-tagline {
    position: absolute; left: 44px; top: 152px;
    font-size: 27px; color: var(--ink); letter-spacing: 2px;
  }
  .holder-name {
    position: absolute; right: 44px; top: 118px;
    font-size: 40px; font-weight: 700; color: var(--brand-green);
  }
  .divider {
    position: absolute; left: 44px; right: 44px; top: 200px;
    height: 2px; background: var(--ink);
  }
  .company {
    position: absolute; left: 44px; top: 232px;
    font-size: 29px; font-weight: 700; color: var(--ink);
  }
  .contact-list {
    position: absolute; left: 44px; top: 288px; list-style: none;
  }
  .contact-list li {
    display: flex; align-items: center; gap: 16px;
    height: 44px; font-size: 26px; color: var(--ink);
  }
  .contact-list li.web { color: var(--brand-green); }
  .contact-icon {
    width: 32px; height: 32px; border-radius: 6px; background: var(--brand-green);
    display: flex; align-items: center; justify-content: center; flex: none;
  }
  .contact-icon svg { width: 20px; height: 20px; }
  .address {
    position: absolute; right: 44px; top: 262px; text-align: right;
    font-size: 25px; color: var(--ink); line-height: 1.45;
  }
</style>
</head>
<body>

<section class="card card-front">
  <div class="front-brand">
    <span class="brand-dot"></span>
    <span class="brand-name">quorvel</span>
  </div>
  <p class="front-tagline">FOCUS. CLARITY. GAIN.</p>
  <p class="front-services">Accountants | Tax Agents | Mortgage Brokers</p>
</section>

<section class="card card-back">
  <div class="back-brand">
    <span class="brand-dot"></span>
    <span class="brand-name">quorvel</span>
  </div>
  <p class="back-tagline">FOCUS. CLARITY. GAIN.</p>
  <p class="holder-name">Dalian Okoruwe</p>
  <div class="divider"></div>
  <p class="company">Quorvel Group Pty Ltd</p>
  <ul class="contact-list">
    <li>
      <span class="contact-icon">
        <svg viewBox="0 0 20 20"><path d="M4 3h4l1.5 4-2 1.3a9 9 0 0 0 4.2 4.2L13 10.5l4 1.5v4a1.5 1.5 0 0 1-1.6 1.5A14 14 0 0 1 2.5 4.6 1.5 1.5 0 0 1 4 3z" fill="#fff"/></svg>
      </span>07 3184 5526
    </li>
    <li>
      <span class="contact-icon">
        <svg viewBox="0 0 20 20"><rect x="6" y="2" width="8" height="5" fill="#fff"/><rect x="2" y="7" width="16" height="7" rx="1.5" fill="#fff"/><rect x="6" y="12" width="8" height="6" fill="#fff" stroke="#7dc242" stroke-width="1"/></svg>
      </span>07 3952 1087
    </li>
    <li>
      <span class="contact-icon">
        <svg viewBox="0 0 20 20"><rect x="2" y="4" width="16" height="12" fill="#fff"/><path d="M2 4l8 7 8-7" fill="none" stroke="#7dc242" stroke-width="1.5"/></svg>
      </span>dokoruwe@quorvel.net.au
    </li>
    <li class="web">
      <span class="contact-icon">
        <svg viewBox="0 0 20 20" fill="none" stroke="#fff" stroke-width="1.5"><circle cx="10" cy="10" r="7.5"/><ellipse cx="10" cy="10" rx="3.2" ry="7.5"/><path d="M2.5 10h15M4 6h12M4 14h12"/></svg>
      </span>www.quorvel.net.au
    </li>
  </ul>
  <p class="address">3/412 Brackwin Rd Halvern QLD 4219<br>PO Box 829 Halvern QLD 4219</p>
</section>

</body>
</html>
```